Real Estate Advertising Window Card

Looking for an A3 poster to advertise individual staff from our office. We want it to have sections on personal passions &/or hobbies, a bit about their family, personal awards &/or achievements, how long they've been in real estate and a testimonial from scoreyourbroker.com.au The poster will have a profile photo of the Agent as well as at least one personal/family photo.

Target Market(s)

People looking to sell or rent out their property

Industry/Entity Type

Real Estate

Font styles to use
Sans Serif

Colors
0792cd
f37022

Requirements
Must have
• Must be delivered in a format that we can modify (preferably in MS Publisher). Must be eye catching - not too wordy. Make people want to read and take notice of it. Must have staff member name and contact details.
• sections on personal passions &/or hobbies, a bit about their family, personal awards &/or achievements, how long they've been in real estate and a testimonial from scoreyourbroker.com.au The poster will have a profile photo of the Agent as well as at least one personal/family photo.

```html
<!DOCTYPE html>
<html lang="en">
<head>
<meta charset="utf-8">
<title>Daniel Marsh – Agent Window Card</title>
<link href="https://fonts.googleapis.com/css2?family=Lato:ital,wght@0,300;0,400;0,700;1,400;1,700&family=Montserrat:wght@700&display=swap" rel="stylesheet">
<style>
:root{
  --paper:#ececec;
  --charcoal:#3a3b3e;
  --slate:#343a44;
  --orange:#e2691f;
  --ink:#2b2b2b;
  --muted:#666;
  --heading:#7a7a7a;
  --frame:#c9c9c9;
  --gold:#d9a514;
  --white:#ffffff;
}
*{margin:0;padding:0;box-sizing:border-box}
html,body{width:691px;height:1200px;overflow:hidden;background:var(--paper)}
body{font-family:'Lato',sans-serif;color:var(--ink);position:relative}
.abs{position:absolute}
.top-band{left:0;top:0;width:691px;height:95px;background:var(--paper)}
.name-band{left:0;top:95px;width:691px;height:188px;background:var(--charcoal)}
.intro-band{left:0;top:283px;width:691px;height:122px;background:var(--orange)}
.band-notch{left:270px;top:94px}
.portrait-frame{left:33px;top:39px;width:219px;height:330px;background:var(--frame);padding:7px}
.portrait{width:100%;height:100%;background:linear-gradient(180deg,#f4f4f4 0%,#e6e6e6 45%,#5b5f66 75%,#44484f 100%)}
.contact{display:flex;align-items:center;gap:9px;top:46px}
.contact-phone{left:284px}
.contact-email{left:455px}
.contact-label{font-size:10px;color:#555;line-height:1.2}
.contact-value{font-size:11.5px;font-weight:700;color:var(--ink)}
.agent-name{left:321px;top:128px;font-family:'Montserrat',sans-serif;font-weight:700;font-size:40px;line-height:52px;letter-spacing:3px;color:var(--white)}
.designation{left:326px;top:244px;font-size:11.5px;font-weight:400;color:#e0e0e0}
.intro-copy{left:281px;top:313px;width:370px;font-size:8.6px;line-height:12.4px;font-weight:400;color:var(--white)}
.section-title{font-weight:300;font-size:17px;letter-spacing:2px;color:var(--heading)}
.about-title{left:59px;top:432px}
.passion{left:59px;width:220px}
.passion h3{font-size:10.5px;font-weight:700;margin-bottom:4px}
.passion p{font-size:8.4px;line-height:11px;font-style:italic;font-weight:400;color:var(--muted)}
.interest-box{left:277px;top:481px;width:149px;height:150px;background:var(--orange);color:var(--white)}
.interest-title{position:absolute;left:28px;top:20px;font-size:13px;font-weight:300;letter-spacing:1.5px;display:flex;align-items:center;gap:3px}
.interest-rule{position:absolute;left:28px;top:46px;width:20px;height:1px;background:var(--white)}
.hobby{position:absolute;width:36px;text-align:center;font-size:5.5px;letter-spacing:.3px}
.hobby svg{display:block;margin:0 auto 3px}
.family-photo{left:60px;top:677px;width:222px;height:154px;border:2px solid #d6d6d6;background:linear-gradient(135deg,#e9e9e9 0%,#cfc9c4 40%,#8f9fb5 70%,#3b58a8 100%)}
.family-copy{left:294px;top:677px;width:142px;font-size:8.4px;line-height:12.4px;font-style:italic;font-weight:400;color:var(--muted);text-align:justify}
.family-copy p+p{margin-top:9px}
.testimonials-title{left:62px;top:893px}
.testimonial{left:70px;width:350px}
.testimonial h4{font-size:13.5px;font-weight:700;font-style:italic;margin-bottom:5px}
.testimonial p{font-size:7.9px;line-height:10.6px;font-style:italic;font-weight:400;color:var(--muted)}
.testimonial p+p{margin-top:10px}
.profile-panel{left:454px;top:417px;width:209px;height:633px;background:var(--slate);color:var(--white)}
.panel-title{position:absolute;left:0;width:100%;text-align:center;font-size:16px;font-weight:300;letter-spacing:1.5px;line-height:23px}
.panel-title span{border-bottom:1px solid var(--white)}
.profile-copy{position:absolute;left:25px;top:70px;width:170px;font-size:8.2px;line-height:11.1px;font-weight:400;text-align:justify}
.profile-copy p+p{margin-top:10px}
.award{position:absolute;left:16px;display:flex;align-items:flex-start;gap:9px;width:185px}
.award-mark{width:20px;font-size:14px;font-weight:300;text-align:center;flex:none;line-height:18px}
.award p{font-size:7.9px;line-height:10.6px;font-style:italic;font-weight:400}
.brand{left:478px;top:1118px;display:flex;align-items:center;gap:8px;color:var(--ink)}
.brand-dot{width:12px;height:12px;border-radius:50%;background:var(--orange);flex:none}
.brand-name{font-size:26px;font-weight:700;line-height:30px}
</style>
</head>
<body>

<div class="abs top-band"></div>
<div class="abs name-band"></div>
<div class="abs intro-band"></div>
<svg class="abs band-notch" width="14" height="8" viewBox="0 0 14 8"><polygon points="0,0 14,0 7,7" fill="var(--paper)"/></svg>

<div class="abs portrait-frame"><div class="portrait" role="img" aria-label="Portrait photo of the agent in a grey suit"></div></div>

<div class="abs contact contact-phone">
  <svg width="36" height="36" viewBox="0 0 36 36"><circle cx="18" cy="18" r="17" fill="var(--orange)"/><path d="M12 10c1-1 2-1 3 0l2 3c.5 1 .3 2-.5 2.6l-1 .8c.8 2 2.3 3.6 4.3 4.4l.8-1c.6-.8 1.6-1 2.6-.5l3 2c1 .6 1 1.8 0 2.8l-1.3 1.3c-1.3 1.3-3.5 1.3-6-.3-3-2-5.8-4.8-7.7-7.8-1.6-2.5-1.6-4.7-.3-6z" fill="var(--white)"/></svg>
  <div><div class="contact-label">Mobile:</div><div class="contact-value">+123-456-0192</div></div>
</div>
<div class="abs contact contact-email">
  <svg width="36" height="36" viewBox="0 0 36 36"><circle cx="18" cy="18" r="17" fill="var(--orange)"/><circle cx="18" cy="18" r="14" fill="none" stroke="var(--white)" stroke-width="1.2"/><rect x="10" y="12" width="16" height="12" rx="1" fill="none" stroke="var(--white)" stroke-width="1.6"/><path d="M10 13l8 6 8-6" fill="none" stroke="var(--white)" stroke-width="1.6"/></svg>
  <div><div class="contact-label">Email</div><div class="contact-value">daniel.marsh@email.com</div></div>
</div>

<h1 class="abs agent-name">DANIEL<br>MARSH</h1>
<div class="abs designation">Designation/ Job Position</div>

<p class="abs intro-copy">Lorem Ipsum is simply dummy text of the printing and typesetting industry. Lorem Ipsum has been the industry's standard dummy text ever since the 1500s, when an unknown printer took a galley of type and scrambled it to make a type specimen book. It has survived not only five centuries, but also the leap into electronic typesetting, remaining essentially unchanged..</p>

<h2 class="abs section-title about-title">ABOUT ME</h2>
<div class="abs passion" style="top:482px"><h3>Passion - 01</h3><p>Lorem Ipsum is simply dummy text of the printing<br>and typesetting industry. Lorem Ipsum has been.</p></div>
<div class="abs passion" style="top:545px"><h3>Passion - 02</h3><p>Lorem Ipsum is simply dummy text of the printing<br>and typesetting industry. Lorem Ipsum has been.</p></div>
<div class="abs passion" style="top:602px"><h3>Passion - 03</h3><p>Lorem Ipsum is simply dummy text of the printing<br>and typesetting industry. Lorem Ipsum has been.</p></div>

<div class="abs interest-box">
  <svg style="position:absolute;left:24px;top:-6px" width="12" height="7" viewBox="0 0 12 7"><polygon points="0,7 12,7 6,0" fill="var(--orange)"/></svg>
  <div class="interest-title"><svg width="13" height="12" viewBox="0 0 13 12"><path d="M6.5 11L1.5 6C0 4.5.3 2 2.2 1.2 3.8.6 5.5 1.3 6.5 2.7 7.5 1.3 9.2.6 10.8 1.2 12.7 2 13 4.5 11.5 6z" fill="none" stroke="var(--white)" stroke-width="1.1"/></svg>INTEREST</div>
  <div class="interest-rule"></div>
  <div class="hobby" style="left:19px;top:65px"><svg width="14" height="14" viewBox="0 0 14 14"><circle cx="7" cy="7" r="6" fill="none" stroke="#fff" stroke-width="1.4"/><polygon points="7,4.5 9.3,6.2 8.4,8.8 5.6,8.8 4.7,6.2" fill="#fff"/></svg>FOOTBALL</div>
  <div class="hobby" style="left:57px;top:65px"><svg width="14" height="14" viewBox="0 0 14 14"><path d="M1 8l5-1 3-5c.5-1 2-1 1.6.3L9 7l4 1v1.5L8.5 9.5 6 13H4.8l1.5-3.5L2 9.5z" fill="#fff"/></svg>TRAVEL</div>
  <div class="hobby" style="left:95px;top:65px"><svg width="14" height="14" viewBox="0 0 14 14"><rect x="1.5" y="1.5" width="11" height="11" fill="none" stroke="#fff" stroke-width="1.4"/><rect x="4.5" y="4" width="5" height="6" fill="#fff"/></svg>MOVIES</div>
  <div class="hobby" style="left:19px;top:102px"><svg width="16" height="12" viewBox="0 0 16 12"><path d="M3 2h10c2 0 3 3 3 6s-2 4-3.5 2L11 8H5L3.5 10C2 12 0 11 0 8s1-6 3-6z" fill="#fff"/></svg>GAMES</div>
  <div class="hobby" style="left:57px;top:102px"><svg width="14" height="12" viewBox="0 0 14 12"><path d="M1 3h3l1.5-2h3L10 3h3v8H1z" fill="#fff"/><circle cx="7" cy="7" r="2.3" fill="var(--orange)"/></svg>PHOTO</div>
  <div class="hobby" style="left:95px;top:100px"><svg width="12" height="14" viewBox="0 0 12 14"><polygon points="6,0 10,5 8,5 11,9 7,9 7,14 5,14 5,9 1,9 4,5 2,5" fill="#fff"/></svg>BEAUTY</div>
</div>

<div class="abs family-photo" role="img" aria-label="Family photo of the agent with partner and baby"></div>
<div class="abs family-copy">
  <p>Lorem Ipsum is simply dummy text of the printing and typesetting industry. Lorem Ipsum has been the industry's standard dummy text ever since the 1500s, when an unknown printer took a galley of type and scrambled it to make a type specimen book.</p>
  <p>There are many variations of passages of Lorem Ipsum available, but the majority have suffered alteration in some form.</p>
</div>

<h2 class="abs section-title testimonials-title">TESTIMONIALS</h2>
<div class="abs testimonial" style="top:940px">
  <h4>“Daniel is an excellent agent”</h4>
  <p>Daniel leads a team of professional agents and he is an outstanding agent himself. My property was a challenge to sell in the current market. An older apartment against new, fresh apartments and older apartments with stronger yields in the inner south market. Daniel and his team were on point from even before the listing with delicate management of the tenant and then full stream ahead with the marketing. Daniel engaged the potential investors and owner occupiers to qualify their interest and he kept me up-to-date. His approach was excellent</p>
</div>
<div class="abs testimonial" style="top:1058px">
  <h4>“Daniel and the team nailed it!”</h4>
  <p>Daniel, Sophie and the Oliver Grant team made a very stressfull time a breeze! I would not hesitate to recommend Daniel and the team for the sale of your home or investment property.</p>
  <p>Thanks for all your hard work and for keeping my stress levels to a minumum.</p>
</div>

<aside class="abs profile-panel">
  <h2 class="panel-title" style="top:30px"><span>PROFILE</span></h2>
  <div class="profile-copy">
    <p>Lorem Ipsum is simply dummy text of the printing and typesetting industry. Lorem Ipsum has been the industry's standard dummy text ever since the 1500s, when an unknown printer took a galley of type and scrambled it to make a type specimen book.</p>
    <p>It has survived not only five centuries, but also the leap into electronic typesetting, remaining essentially unchanged..</p>
    <p>There are many variations of passages of Lorem Ipsum available, but the majority have suffered alteration in some form, by injected humour, or randomised words which don't look even slightly believable.</p>
  </div>
  <h2 class="panel-title" style="top:304px"><span>ACHIEVEMENTS/</span><br><span>AWARDS</span></h2>
  <div class="award" style="top:362px"><span class="award-mark">01</span><p>Lorem Ipsum is simply dummy text of the printing and typesetting industry. Lorem</p></div>
  <div class="award" style="top:405px"><span class="award-mark">02</span><p>Lorem Ipsum is simply dummy text of the printing and typesetting industry. Lorem</p></div>
  <div class="award" style="top:448px"><span class="award-mark">03</span><p>Lorem Ipsum is simply dummy text of the printing and typesetting industry. Lorem</p></div>
  <div class="award" style="top:495px"><span class="award-mark"><svg width="18" height="22" viewBox="0 0 18 22"><path d="M4 1h10v6c0 3-2 5-5 5s-5-2-5-5z M4 3H1c0 3 1 5 3.5 5.5 M14 3h3c0 3-1 5-3.5 5.5" fill="var(--gold)" stroke="var(--gold)" stroke-width="1.2"/><rect x="8" y="12" width="2" height="5" fill="var(--gold)"/><rect x="4.5" y="17" width="9" height="3" fill="var(--gold)"/></svg></span><p>Lorem Ipsum is simply dummy text of the printing and typesetting industry. Lorem</p></div>
  <div class="award" style="top:541px"><span class="award-mark"><svg width="18" height="22" viewBox="0 0 18 22"><path d="M4 1h10v6c0 3-2 5-5 5s-5-2-5-5z M4 3H1c0 3 1 5 3.5 5.5 M14 3h3c0 3-1 5-3.5 5.5" fill="var(--gold)" stroke="var(--gold)" stroke-width="1.2"/><rect x="8" y="12" width="2" height="5" fill="var(--gold)"/><rect x="4.5" y="17" width="9" height="3" fill="var(--gold)"/></svg></span><p>Lorem Ipsum is simply dummy text of the printing and typesetting industry. Lorem</p></div>
  <div class="award" style="top:592px"><span class="award-mark"><svg width="18" height="22" viewBox="0 0 18 22"><path d="M4 1h10v6c0 3-2 5-5 5s-5-2-5-5z M4 3H1c0 3 1 5 3.5 5.5 M14 3h3c0 3-1 5-3.5 5.5" fill="var(--gold)" stroke="var(--gold)" stroke-width="1.2"/><rect x="8" y="12" width="2" height="5" fill="var(--gold)"/><rect x="4.5" y="17" width="9" height="3" fill="var(--gold)"/></svg></span><p>Lorem Ipsum is simply dummy text of the printing and typesetting industry. Lorem</p></div>
</aside>

<div class="abs brand">
  <span class="brand-dot"></span>
  <span class="brand-name">Harbourline</span>
</div>

</body>
</html>
```